Kestrel Ridge Partners LLC
Business card and stationary set for Investment Firm - Financial Services
Business card and stationary set for Investment Firm
Simple
Owen Talcott
President / Founder
4820 Birchwood Lane Sparta, IL 62286
owen@talcottwealth.example
www.talcottwealth.example
jdalvin jdalvin
Also, please keep a simple, prestigious / exclusive look to the design.
Designers- I am looking for a design that uses watermarks and different parts of the logo separated out to create some originality. I only want to see the the "Professional Investment Management" one time in the design with the logo. Also, there are 2 formats of the logo in the files I uploaded. One has the graphic on the side and the other on the top. I'd like to see the use of both of these. I do like the blue on the back of the card...maybe a watermark included. The most creative will probably get the win on this. Thank you.
bluequill bluequill
Can u do some sort of star rating, which help us to make these changes,and then i will submit you stationary package with your requirements.. thanks
Also, thank you cards.
Designers - A few things I'll need in the design will be the removal of "Professional Investment Management" from the logo on the front of the card. I still like it to be on the back OR on the larger logo. I only wanted it listed on one of the logos as opposed to both of them. Also, I do like the look and feel of an exclusive, simple, unique design. I do like the back side of the card to be the blue color. I like a background image of the logo as well to add texture. Finally, I need a full stationary design including letterhead, envelopes and return of all sizes (standard and 10X 13), business cards, folders and 1/4 page paper pad. Thank you.
Vandal Vandal
Star Rating please....
Also, please include simple envelope design
Be sure to include standard stationary design as well. The font does not need to be the same as the logo on all pieces.
Designers - Feel free to remove the tagline "Professional Investment Management" in parts of the stationary and business cards. It can be included but isn't necessary. Thank you.

```html
<!DOCTYPE html>
<html lang="en">
<head>
<meta charset="utf-8">
<title>Kestrel Ridge Partners LLC – Business Card</title>
<link rel="stylesheet" href="https://fonts.googleapis.com/css2?family=Cinzel:wght@400;500&family=Open+Sans:ital,wght@0,400;0,600;1,300&display=swap">
<style>
  :root {
    --bg: #e6e4e0;
    --teal: #1f6678;
    --teal-light: #2b7a8d;
    --teal-dark: #17515f;
    --white: #ffffff;
    --ink-grey: #8a8f93;
    --shadow: rgba(0, 0, 0, 0.22);
  }
  * { margin: 0; padding: 0; box-sizing: border-box; }
  html, body {
    width: 1200px;
    height: 576px;
    overflow: hidden;
    background: var(--bg);
  }
  .canvas {
    position: relative;
    width: 1200px;
    height: 576px;
    display: flex;
    align-items: center;
    justify-content: center;
    gap: 50px;
  }
  .card {
    position: relative;
    width: 530px;
    height: 306px;
    overflow: hidden;
    box-shadow: 0 8px 22px var(--shadow);
  }

  /* Back of card */
  .card-back {
    background: linear-gradient(135deg, var(--teal-light) 0%, var(--teal) 45%, var(--teal-dark) 100%);
    display: flex;
    flex-direction: column;
    align-items: center;
    justify-content: center;
    color: var(--white);
  }
  .card-back .company {
    font-family: "Cinzel", serif;
    font-size: 27px;
    font-weight: 400;
    letter-spacing: 0.5px;
  }
  .card-back .web {
    margin-top: 6px;
    font-family: "Open Sans", sans-serif;
    font-size: 13px;
    letter-spacing: 1.5px;
  }

  /* Front of card */
  .card-front { background: var(--white); }
  .front-header {
    position: absolute;
    left: 30px;
    top: 24px;
  }
  .front-header .company {
    font-family: "Cinzel", serif;
    font-size: 25px;
    color: var(--teal);
    letter-spacing: 0.3px;
  }
  .front-header .tagline {
    font-family: "Open Sans", sans-serif;
    font-size: 8px;
    color: var(--ink-grey);
    letter-spacing: 2px;
    text-transform: uppercase;
    margin-top: 1px;
  }
  .person {
    position: absolute;
    left: 30px;
    top: 78px;
  }
  .person .name {
    font-family: "Open Sans", sans-serif;
    font-style: italic;
    font-weight: 300;
    font-size: 17px;
    color: var(--ink-grey);
  }
  .person .role {
    font-family: "Open Sans", sans-serif;
    font-size: 10px;
    color: var(--ink-grey);
    margin-top: 1px;
  }
  .band {
    position: absolute;
    left: 0;
    right: 0;
    top: 140px;
    bottom: 0;
    background: linear-gradient(160deg, var(--teal-light) 0%, var(--teal) 50%, var(--teal-dark) 100%);
  }
  .contact {
    position: absolute;
    left: 320px;
    top: 176px;
    font-family: "Open Sans", sans-serif;
    font-size: 13px;
    line-height: 18px;
    color: var(--white);
  }
  .contact .address { margin-bottom: 10px; }
  .contact .line {
    display: flex;
    align-items: center;
    gap: 6px;
  }
  .contact .icon { width: 12px; height: 12px; flex: none; }
  .contact .web { margin-top: 6px; }
</style>
</head>
<body>
<main class="canvas">
  <section class="card card-back" aria-label="Business card back">
    <div class="company">Kestrel Ridge Partners LLC</div>
    <div class="web">www.talcottwealth.example</div>
  </section>

  <section class="card card-front" aria-label="Business card front">
    <header class="front-header">
      <div class="company">Kestrel Ridge Partners LLC</div>
      <div class="tagline">Professional Investment Management</div>
    </header>
    <div class="person">
      <div class="name">Owen Talcott</div>
      <div class="role">President / Founder</div>
    </div>
    <div class="band"></div>
    <address class="contact">
      <div class="address">4820 Birchwood Lane<br>Sparta, IL 62286</div>
      <div class="line">
        <svg class="icon" viewBox="0 0 12 12" aria-hidden="true">
          <path d="M2.5 1h2l1 2.6-1.3 1a6 6 0 0 0 3.2 3.2l1-1.3L11 7.5v2A1.5 1.5 0 0 1 9.5 11 8.5 8.5 0 0 1 1 2.5 1.5 1.5 0 0 1 2.5 1z" fill="var(--white)"/>
        </svg>
        <span>(618) 555-0147</span>
      </div>
      <div class="line">
        <svg class="icon" viewBox="0 0 12 12" aria-hidden="true">
          <rect x="0.5" y="2" width="11" height="8" rx="1" fill="var(--white)"/>
          <path d="M1 2.6l5 3.8 5-3.8" fill="none" stroke="var(--teal)" stroke-width="1"/>
        </svg>
        <span>owen@talcottwealth.example</span>
      </div>
      <div class="web">www.talcottwealth.example</div>
    </address>
  </section>
</main>
</body>
</html>
```